Splashy Door Hanger

I am wanting a new design done for our window cleaning business. It is mainly the theme that I wouldn't mind exploring and experimenting with: the complimentary colours, the backgrounds, the text, etc. The water droplets are re-used frequently in our vehicle decals, print ads, etc so we would probably like to keep at least a small amount of them.

We want the final product to professional looking, fun and splashy--as you might expect from a progressive cleaning company.

Final deliverables must include two PSD files with all layers still visible (one for each side of doorhanger) using the template included for quikpressly.ca.

The current files and a new group photo can be found here: https://files.vantorebox.com/open?id=7rKqLmZtWx2NpHd9YsVbCe4JfGaUoTnRi . Additionally, you can visit our website to get a feel for our current look: http://brightpanewash.ca

Target Market(s)

Middle income men and women age 40-60

Industry/Entity Type

Business

Requirements
Must have
• 3 phone numbers, website, logo
Nice to have
• Droplet background (somewhere)

```html
<!DOCTYPE html>
<html lang="en">
<head>
<meta charset="utf-8">
<title>BrightPane Wash Door Hanger</title>
<link href="https://fonts.googleapis.com/css2?family=Ubuntu:wght@400;500;700&display=swap" rel="stylesheet">
<style>
  :root {
    --navy: #1c3a8f;
    --navy-deep: #14286b;
    --cyan: #17a8e0;
    --yellow: #f7d21a;
    --red: #e0202a;
    --ink: #1a1a1a;
    --grey: #7a7a7a;
    --paper: #ffffff;
    --stage: #e9e9e9;
    --gold: #d9a92a;
  }
  html, body { margin: 0; padding: 0; overflow: hidden; }
  body {
    width: 1169px; height: 1200px; background: var(--stage);
    font-family: "Ubuntu", sans-serif; position: relative;
  }
  .hanger {
    position: absolute; top: 79px; width: 430px; height: 1050px;
    background: var(--paper); overflow: hidden;
    box-shadow: 0 4px 14px rgba(0,0,0,.25);
  }
  .hanger--front { left: 121px; }
  .hanger--back { left: 630px; }
  .hanger > * { position: absolute; }
  .shapes { left: 0; top: 0; width: 430px; height: 1050px; }
  .photo-main { left: 0; top: 0; width: 430px; height: 380px;
    background: linear-gradient(160deg, #8e9a8a 0%, #5b6a62 40%, #3f4f5a 70%, #7f8b7a 100%); }
  .photo-inset { left: 259px; top: 258px; width: 156px; height: 156px; border-radius: 50%;
    border: 3px solid #fff; box-sizing: border-box;
    background: radial-gradient(circle at 50% 40%, #5f8fa8 0%, #4a6a55 60%, #3b5340 100%); }
  .photo-team { left: 0; top: 110px; width: 430px; height: 330px;
    background: linear-gradient(180deg, rgba(255,255,255,0) 0%, #9bb6c9 25%, #3f63b8 60%, #4a5560 100%); }
  .hang-hole { width: 152px; height: 152px; border-radius: 50%; background: var(--stage); left: 136px; top: 49px; }
  .hang-slit { left: 0; top: 124px; width: 140px; height: 2px; background: #333; }
  .header { left: 0; width: 430px; top: 20px; text-align: center; font-weight: 700; font-size: 17.5px; }
  .header--yellow { color: var(--yellow); }
  .header--navy { color: var(--navy); }
  .notice { left: 0; width: 430px; top: 428px; text-align: center; color: #fff; }
  .notice h2 { margin: 0 0 6px; color: var(--yellow); font-size: 26px; font-weight: 700; line-height: 32px; }
  .notice p { margin: 0; font-size: 19px; line-height: 24px; }
  .notice strong { color: var(--yellow); font-weight: 700; }
  .service { left: 18px; width: 396px; }
  .service--gutter { top: 616px; }
  .service--window { top: 752px; }
  .service-head { position: relative; height: 52px; }
  .service-head svg { position: absolute; left: 0; top: 14px; }
  .service-head h3 { position: absolute; left: 59px; top: 18px; margin: 0; font-size: 26px; font-weight: 700; color: var(--ink); }
  .price { position: absolute; right: -2px; top: 0; text-align: right; }
  .price small { display: block; font-size: 15px; color: var(--grey); }
  .price b { display: block; font-size: 31px; color: var(--red); font-weight: 500; line-height: 30px; }
  .service p { margin: 6px 0 0; font-size: 14px; line-height: 19px; letter-spacing: -0.25px; color: var(--ink); text-align: justify; hyphens: auto; }
  .brand { left: 22px; top: 944px; width: 170px; display: flex; align-items: center; gap: 8px; color: #fff; font-weight: 700; font-size: 17px; line-height: 20px; }
  .brand-dot { width: 26px; height: 26px; border-radius: 50%; background: var(--yellow); flex: none; }
  .contacts { left: 218px; top: 946px; margin: 0; padding: 0; list-style: none; color: #fff; font-size: 14.5px; font-weight: 500; }
  .contacts li { height: 22.5px; display: flex; align-items: center; gap: 6px; }
  .contacts .web { color: var(--yellow); }
  .pledge { left: 0; width: 430px; top: 488px; text-align: center; color: var(--yellow); font-size: 21px; font-weight: 700; line-height: 29px; margin: 0; }
  .about { left: 20px; width: 390px; top: 574px; text-align: center; color: #fff; font-size: 15px; line-height: 22px; margin: 0; }
  .insured { left: 0; width: 430px; top: 708px; text-align: center; color: var(--yellow); font-size: 15px; font-weight: 500; margin: 0; }
  .perks { left: 24px; top: 754px; margin: 0; padding: 0; list-style: none; color: #fff; font-size: 15px; font-weight: 700; }
  .perks li { height: 37px; display: flex; align-items: flex-start; gap: 12px; }
  .badge { left: 289px; top: 337px; width: 132px; height: 132px; border-radius: 50%;
    background: radial-gradient(circle, #f3d26a 0%, var(--gold) 65%, #a57a16 100%); }
</style>
</head>
<body>

<section class="hanger hanger--front">
  <div class="photo-main" role="img" aria-label="Worker on a ladder cleaning second-storey windows of a house"></div>
  <svg class="shapes" viewBox="0 0 430 1050" aria-hidden="true">
    <path d="M0,322 C80,360 170,365 260,338 C330,318 392,350 430,395 L430,604 C330,568 250,572 180,588 C110,604 50,590 0,552 Z" fill="var(--cyan)"/>
    <path d="M0,340 C80,378 170,382 262,356 C332,336 392,368 430,412 L430,584 C330,548 250,552 180,572 C110,590 50,575 0,540 Z" fill="var(--navy)"/>
    <path d="M0,950 C110,900 250,870 430,905 L430,1050 L0,1050 Z" fill="var(--navy)"/>
  </svg>
  <div class="photo-inset" role="img" aria-label="Worker kneeling on a roof clearing a gutter"></div>
  <div class="hang-slit"></div>
  <div class="hang-hole"></div>
  <div class="header header--yellow">IT'S MORE AFFORDABLE THAN YOU THINK!</div>

  <div class="notice">
    <h2>JUST A FRIENDLY NOTICE</h2>
    <p>Home maintenance season is here and we<br>are working in your neighbourhood!<br><strong>Call us for your FREE quote today!</strong></p>
  </div>

  <div class="service service--gutter">
    <div class="service-head">
      <svg width="48" height="40" viewBox="0 0 48 40"><rect x="2" y="8" width="30" height="30" fill="none" stroke="var(--ink)" stroke-width="4"/><path d="M8,22 L17,32 L44,2" fill="none" stroke="var(--navy)" stroke-width="6"/></svg>
      <h3>GUTTER CLEANING</h3>
      <div class="price"><small>AVERAGE</small><b>$135</b></div>
    </div>
    <p>An important, yet often forgotten aspect of home maintenance. We scoop out all mud and debris then finish with a flush to make sure your gutter system is functioning properly.</p>
  </div>

  <div class="service service--window">
    <div class="service-head">
      <svg width="48" height="40" viewBox="0 0 48 40"><rect x="2" y="8" width="30" height="30" fill="none" stroke="var(--ink)" stroke-width="4"/><path d="M8,22 L17,32 L44,2" fill="none" stroke="var(--navy)" stroke-width="6"/></svg>
      <h3>WINDOW CLEANING</h3>
      <div class="price"><small>AVERAGE</small><b>$99</b></div>
    </div>
    <p>Treat yourself to professionally cleaned windows! We wash all debris off your exterior glass using a squeegee and finish by wiping down the sills. Deck glass railings $3/pane and screens $3 each.</p>
  </div>

  <div class="brand"><span class="brand-dot"></span>BrightPane Wash</div>
  <ul class="contacts">
    <li><svg width="12" height="12" viewBox="0 0 24 24"><path d="M6.6 10.8a15 15 0 0 0 6.6 6.6l2.2-2.2a1 1 0 0 1 1-.25 11 11 0 0 0 3.6.6 1 1 0 0 1 1 1V20a1 1 0 0 1-1 1A17 17 0 0 1 3 4a1 1 0 0 1 1-1h3.5a1 1 0 0 1 1 1 11 11 0 0 0 .6 3.6 1 1 0 0 1-.25 1Z" fill="var(--yellow)"/></svg>Kelowna 250-555-0142</li>
    <li><svg width="12" height="12" viewBox="0 0 24 24"><path d="M6.6 10.8a15 15 0 0 0 6.6 6.6l2.2-2.2a1 1 0 0 1 1-.25 11 11 0 0 0 3.6.6 1 1 0 0 1 1 1V20a1 1 0 0 1-1 1A17 17 0 0 1 3 4a1 1 0 0 1 1-1h3.5a1 1 0 0 1 1 1 11 11 0 0 0 .6 3.6 1 1 0 0 1-.25 1Z" fill="var(--yellow)"/></svg>Kamloops 250-555-0187</li>
    <li><svg width="12" height="12" viewBox="0 0 24 24"><path d="M6.6 10.8a15 15 0 0 0 6.6 6.6l2.2-2.2a1 1 0 0 1 1-.25 11 11 0 0 0 3.6.6 1 1 0 0 1 1 1V20a1 1 0 0 1-1 1A17 17 0 0 1 3 4a1 1 0 0 1 1-1h3.5a1 1 0 0 1 1 1 11 11 0 0 0 .6 3.6 1 1 0 0 1-.25 1Z" fill="var(--yellow)"/></svg>Salmon Arm 250-555-0163</li>
    <li class="web"><svg width="12" height="12" viewBox="0 0 24 24"><circle cx="12" cy="12" r="10" fill="none" stroke="var(--yellow)" stroke-width="2"/><path d="M2 12h20M12 2c3 3 3 17 0 20M12 2c-3 3-3 17 0 20" fill="none" stroke="var(--yellow)" stroke-width="1.5"/></svg>BrightPaneWash.ca</li>
  </ul>
</section>

<section class="hanger hanger--back">
  <div class="photo-team" role="img" aria-label="Group photo of the cleaning crew in blue uniforms in front of work vans"></div>
  <svg class="shapes" viewBox="0 0 430 1050" aria-hidden="true">
    <path d="M0,405 C110,450 250,440 430,380 L430,1050 L0,1050 Z" fill="var(--cyan)"/>
    <path d="M0,425 C110,470 250,460 430,400 L430,1050 L0,1050 Z" fill="var(--navy)"/>
    <path d="M0,870 C60,940 150,950 260,910 C330,885 390,885 430,900 L430,1050 L0,1050 Z" fill="var(--cyan)"/>
    <path d="M0,890 C60,958 150,968 260,928 C330,903 390,903 430,918 L430,1050 L0,1050 Z" fill="var(--navy-deep)"/>
  </svg>
  <div class="badge" role="img" aria-label="Gold ten year anniversary seal"></div>
  <div class="hang-slit"></div>
  <div class="hang-hole"></div>
  <div class="header header--navy">CALL US TO BOOK YOUR APPOINTMENT TODAY!</div>

  <p class="pledge">We don't want one-time customers,<br>we want customers for life!</p>
  <p class="about">We strive to provide an unparalleled level of service,<br>not just in home maintenance,<br>but service in general. We operate on the basis that<br>we only ask for payment when you are<br>totally satisfied with the job you receive.</p>
  <p class="insured">We are fully insured and SafeCrew Council approved.</p>

  <ul class="perks">
    <li><svg width="26" height="24" viewBox="0 0 26 24"><rect x="1.5" y="5" width="18" height="17" fill="none" stroke="#fff" stroke-width="2.5"/><path d="M5,13 L10,19 L24,2" fill="none" stroke="var(--yellow)" stroke-width="4"/></svg>SUPER QUICK BOOKING</li>
    <li><svg width="26" height="24" viewBox="0 0 26 24"><rect x="1.5" y="5" width="18" height="17" fill="none" stroke="#fff" stroke-width="2.5"/><path d="M5,13 L10,19 L24,2" fill="none" stroke="var(--yellow)" stroke-width="4"/></svg>YOU DON'T HAVE TO BE HOME FOR THE VISIT</li>
    <li><svg width="26" height="24" viewBox="0 0 26 24"><rect x="1.5" y="5" width="18" height="17" fill="none" stroke="#fff" stroke-width="2.5"/><path d="M5,13 L10,19 L24,2" fill="none" stroke="var(--yellow)" stroke-width="4"/></svg>EXPERIENCED AND PROFESSIONAL</li>
  </ul>

  <div class="brand"><span class="brand-dot"></span>BrightPane Wash</div>
  <ul class="contacts">
    <li><svg width="12" height="12" viewBox="0 0 24 24"><path d="M6.6 10.8a15 15 0 0 0 6.6 6.6l2.2-2.2a1 1 0 0 1 1-.25 11 11 0 0 0 3.6.6 1 1 0 0 1 1 1V20a1 1 0 0 1-1 1A17 17 0 0 1 3 4a1 1 0 0 1 1-1h3.5a1 1 0 0 1 1 1 11 11 0 0 0 .6 3.6 1 1 0 0 1-.25 1Z" fill="var(--yellow)"/></svg>Kelowna 250-555-0142</li>
    <li><svg width="12" height="12" viewBox="0 0 24 24"><path d="M6.6 10.8a15 15 0 0 0 6.6 6.6l2.2-2.2a1 1 0 0 1 1-.25 11 11 0 0 0 3.6.6 1 1 0 0 1 1 1V20a1 1 0 0 1-1 1A17 17 0 0 1 3 4a1 1 0 0 1 1-1h3.5a1 1 0 0 1 1 1 11 11 0 0 0 .6 3.6 1 1 0 0 1-.25 1Z" fill="var(--yellow)"/></svg>Kamloops 250-555-0187</li>
    <li><svg width="12" height="12" viewBox="0 0 24 24"><path d="M6.6 10.8a15 15 0 0 0 6.6 6.6l2.2-2.2a1 1 0 0 1 1-.25 11 11 0 0 0 3.6.6 1 1 0 0 1 1 1V20a1 1 0 0 1-1 1A17 17 0 0 1 3 4a1 1 0 0 1 1-1h3.5a1 1 0 0 1 1 1 11 11 0 0 0 .6 3.6 1 1 0 0 1-.25 1Z" fill="var(--yellow)"/></svg>Salmon Arm 250-555-0163</li>
    <li class="web"><svg width="12" height="12" viewBox="0 0 24 24"><circle cx="12" cy="12" r="10" fill="none" stroke="var(--yellow)" stroke-width="2"/><path d="M2 12h20M12 2c3 3 3 17 0 20M12 2c-3 3-3 17 0 20" fill="none" stroke="var(--yellow)" stroke-width="1.5"/></svg>BrightPaneWash.ca</li>
  </ul>
</section>

</body>
</html>
```